CHRISTMAS CARD

We want a Christmas card for wealth managers to issue to high net worth clients. Very classy. Very corporate. The finished printed card will be a5 to fit existing envelopes. the design will also be used as part of a digital card so i need the image in a format for email as well as print. The brand uses a silver (foil block) on its logo and a specific pan tone ref olive green (reference 620). Not too religious and include a quirky message.

Target Market(s)

The target market is clients with investments. Typically more than £100,000 which is why the card needs to be very classy.

Industry/Entity Type

Religious

Requirements
Must have
• logo - but i can't work out how to attach it! i can email it tho. contact me on ruth@tarnwickpr.com

```html
<!DOCTYPE html>
<html lang="en">
<head>
<meta charset="utf-8">
<title>Aldermere Group – Season's Greetings Cards</title>
<link href="https://fonts.googleapis.com/css2?family=Pinyon+Script&display=swap" rel="stylesheet">
<style>
  :root {
    --canvas: #ffffff;
    --olive: #7a6c12;
    --olive-pattern: #85781f;
    --festive-red: #ec1c24;
    --red-pattern: #ef3a40;
    --ink-light: #ffffff;
    --script: "Pinyon Script", cursive;
  }
  * { margin: 0; padding: 0; box-sizing: border-box; }
  html, body {
    width: 1200px; height: 1000px;
    overflow: hidden;
    background: var(--canvas);
  }
  .canvas { position: relative; width: 1200px; height: 1000px; }

  .card {
    position: absolute;
    left: 291px;
    width: 621px;
    height: 437px;
    overflow: hidden;
  }
  .card--christmas { top: 17px; background: var(--festive-red); }
  .card--new-year  { top: 542px; background: var(--festive-red); }

  .pattern-field { position: absolute; left: 0; top: 0; width: 100%; }
  .card--christmas .pattern-field {
    height: 359px;
    background: linear-gradient(180deg, var(--olive-pattern), var(--olive));
  }
  .card--new-year .pattern-field {
    height: 100%;
    background: linear-gradient(180deg, var(--red-pattern), var(--festive-red));
  }

  .greeting {
    position: absolute;
    font-family: var(--script);
    font-weight: 400;
    color: var(--ink-light);
    line-height: 1;
    white-space: nowrap;
  }
  .greeting--merry     { left: 30px;  top: 28px;  font-size: 168px; }
  .greeting--christmas { left: 40px;  top: 178px; font-size: 128px; }

  .greeting--wishing    { left: 392px; top: 16px;  font-size: 58px; }
  .greeting--happiness  { left: 12px;  top: 30px;  font-size: 112px; }
  .greeting--ampersand  { left: 398px; top: 104px; font-size: 56px; }
  .greeting--prosperity { left: 178px; top: 128px; font-size: 118px; }
  .greeting--for-the    { left: 12px;  top: 210px; font-size: 58px; }
  .greeting--new        { left: 16px;  top: 284px; font-size: 128px; }
  .greeting--year       { left: 252px; top: 252px; font-size: 122px; }

  .brand-name {
    position: absolute;
    left: 22px;
    top: 382px;
    font-family: var(--script);
    font-size: 34px;
    color: var(--ink-light);
    line-height: 1;
    white-space: nowrap;
  }
</style>
</head>
<body>
<main class="canvas">

  <section class="card card--christmas" aria-label="Christmas greeting card">
    <div class="pattern-field" role="img" aria-label="Repeating small snowflake pattern on olive green"></div>
    <h1 class="greeting greeting--merry">Merry</h1>
    <p class="greeting greeting--christmas">Christmas</p>
    <p class="brand-name">Aldermere Group</p>
  </section>

  <section class="card card--new-year" aria-label="New Year greeting card">
    <div class="pattern-field" role="img" aria-label="Repeating small snowflake pattern on red"></div>
    <p class="greeting greeting--happiness">Happiness</p>
    <p class="greeting greeting--wishing">wishing</p>
    <p class="greeting greeting--ampersand">&amp;</p>
    <p class="greeting greeting--prosperity">Prosperity</p>
    <p class="greeting greeting--for-the">for the</p>
    <p class="greeting greeting--new">New</p>
    <p class="greeting greeting--year">Year</p>
  </section>

</main>
</body>
</html>
```